Bref créative
RKT Stationery
B-Cards
I need double sided standard sized Business Card [3.5" x 2"]
Arial, Arial Black, Comic Sans MS, Courier New, Impact, Trebuchet MS and Verdana
Professional
Dorian Vasko
Operations Manager
P.O. BOX 817
Harlow Point, MD 20999
dorian@rktbuilders.example
www.rktbuilders.example
Doesn't have to include all the information.
Atleast Company name, Logo, persons name and title.
Office number, cell, fax, and e-mail
Could have a calendar of the year, maybe QR codes for website, cell or e-mails of contact.
Anything else that could maybe go on the back of the card. I just don't want it to be blank.
vector logo file

```html
<!DOCTYPE html>
<html lang="en">
<head>
<meta charset="utf-8">
<title>RKT Stationery</title>
<link href="https://fonts.googleapis.com/css2?family=Open+Sans:wght@400;700&display=swap" rel="stylesheet">
<style>
  :root {
    --backdrop: #e9e6e2;
    --paper: #ffffff;
    --brand-red: #9e1b20;
    --brand-red-deep: #6f1014;
    --brand-green: #2f6b2b;
    --flap-grey: #eeeeee;
    --ink: #4a4a4a;
    --shadow: 0 3px 10px rgba(0,0,0,.28);
  }
  * { margin: 0; padding: 0; box-sizing: border-box; }
  html, body { width: 1200px; height: 466px; overflow: hidden; }
  body {
    background: var(--backdrop);
    font-family: "Open Sans", Arial, sans-serif;
    color: var(--ink);
    position: relative;
  }
  .sheet {
    position: absolute;
    background: var(--paper);
    box-shadow: var(--shadow);
    overflow: hidden;
  }
  .sheet > svg.art { position: absolute; inset: 0; width: 100%; height: 100%; }
  .brand {
    position: absolute;
    display: flex;
    align-items: center;
    gap: 5px;
    font-weight: 700;
    color: var(--brand-red);
    white-space: nowrap;
    line-height: 1;
  }
  .brand-mark { background: var(--brand-green); flex: none; }
  .brand-centered { left: 50%; transform: translateX(-50%); }

  .card-front { left: 28px; top: 160px; width: 112px; height: 64px; }
  .card-back  { left: 28px; top: 250px; width: 112px; height: 64px; }
  .card-front .brand { left: 8px; top: 8px; font-size: 6px; gap: 4px; }
  .card-front .brand-mark { width: 6px; height: 6px; }
  .card-person { position: absolute; left: 8px; top: 22px; font-size: 4.5px; line-height: 1.4; }
  .card-person strong { color: var(--brand-red); font-size: 5.5px; }
  .card-back .brand { top: 24px; font-size: 8px; }
  .card-back .brand-mark { width: 8px; height: 8px; }

  .letterhead { top: 38px; width: 288px; height: 384px; }
  .letterhead-one { left: 163px; }
  .letterhead-two { left: 461px; }
  .letterhead .brand { top: 24px; font-size: 9px; }
  .letterhead .brand-mark { width: 9px; height: 9px; }
  .letterhead-contact {
    position: absolute; left: 18px; bottom: 22px;
    font-size: 5.5px; line-height: 1.45;
  }
  .letterhead-watermark {
    position: absolute; left: 132px; top: 150px; transform: translateX(-50%);
    font-size: 22px; font-weight: 700; color: var(--brand-red);
    opacity: .08; white-space: nowrap;
  }

  .envelope-back  { left: 775px; top: 43px;  width: 401px; height: 178px; }
  .envelope-front { left: 782px; top: 233px; width: 394px; height: 84px; }
  .envelope-small { left: 778px; top: 329px; width: 230px; height: 120px; }
  .envelope-back .brand { top: 120px; font-size: 8px; }
  .envelope-back .brand-mark { width: 8px; height: 8px; }
  .envelope-front .brand { top: 38px; font-size: 8px; }
  .envelope-front .brand-mark { width: 8px; height: 8px; }
  .envelope-small .brand { left: 12px; top: 14px; font-size: 7px; }
  .envelope-small .brand-mark { width: 7px; height: 7px; }
  .envelope-return {
    position: absolute; left: 12px; top: 30px; font-size: 5px; line-height: 1.45;
  }
</style>
</head>
<body>

  <section class="sheet card-front">
    <svg class="art" viewBox="0 0 112 64" preserveAspectRatio="none">
      <path d="M112 0 V64 H70 C92 50 102 28 112 0 Z" fill="var(--brand-red)"/>
      <path d="M112 34 V64 H82 C96 58 106 48 112 34 Z" fill="var(--brand-green)"/>
    </svg>
    <div class="brand"><span class="brand-mark"></span>RKT Builders</div>
    <div class="card-person">
      <strong>Dorian Vasko</strong><br>
      Operations Manager<br>
      P.O. BOX 817<br>
      dorian@rktbuilders.example
    </div>
  </section>

  <section class="sheet card-back">
    <svg class="art" viewBox="0 0 112 64" preserveAspectRatio="none">
      <path d="M0 50 C40 40 80 46 112 36 V64 H0 Z" fill="var(--brand-green)"/>
      <path d="M0 54 C40 46 80 52 112 42 V46 C80 56 40 50 0 58 Z" fill="var(--brand-red)"/>
    </svg>
    <div class="brand brand-centered"><span class="brand-mark"></span>RKT Builders</div>
  </section>

  <section class="sheet letterhead letterhead-one">
    <svg class="art" viewBox="0 0 288 384" preserveAspectRatio="none">
      <path d="M288 0 H252 C266 120 262 270 196 384 H288 Z" fill="var(--brand-red)"/>
      <path d="M258 0 H252 C266 120 262 270 196 384 H204 C268 270 272 120 258 0 Z" fill="var(--brand-red-deep)"/>
      <path d="M288 250 C276 320 250 360 214 384 H288 Z" fill="var(--brand-green)"/>
    </svg>
    <div class="brand brand-centered"><span class="brand-mark"></span>RKT Builders</div>
    <div class="letterhead-contact">
      Tel: 301 555 0142<br>
      Fax: 301 555 0143<br>
      P.O. BOX 817<br>
      Harlow Point, MD 20999<br>
      www.rktbuilders.example
    </div>
  </section>

  <section class="sheet letterhead letterhead-two">
    <svg class="art" viewBox="0 0 288 384" preserveAspectRatio="none">
      <path d="M288 40 C268 140 270 220 288 290 Z" fill="var(--brand-red)"/>
      <path d="M0 330 C100 300 200 322 288 282 V384 H0 Z" fill="var(--brand-green)"/>
      <path d="M0 346 C110 318 200 334 288 298 V310 C200 346 110 334 0 360 Z" fill="var(--brand-red)"/>
    </svg>
    <div class="brand brand-centered"><span class="brand-mark"></span>RKT Builders</div>
    <div class="letterhead-watermark">RKT Builders</div>
  </section>

  <section class="sheet envelope-back">
    <svg class="art" viewBox="0 0 401 178" preserveAspectRatio="none">
      <path d="M0 0 H401 V64 C300 40 100 40 0 64 Z" fill="var(--brand-red)"/>
      <path d="M0 64 C100 40 300 40 401 64 V84 C300 62 100 62 0 84 Z" fill="var(--brand-green)"/>
    </svg>
    <div class="brand brand-centered"><span class="brand-mark"></span>RKT Builders</div>
  </section>

  <section class="sheet envelope-front">
    <svg class="art" viewBox="0 0 394 84" preserveAspectRatio="none">
      <path d="M0 0 H394 V10 C260 4 130 4 0 10 Z" fill="var(--flap-grey)"/>
    </svg>
    <div class="brand brand-centered"><span class="brand-mark"></span>RKT Builders</div>
  </section>

  <section class="sheet envelope-small">
    <svg class="art" viewBox="0 0 230 120" preserveAspectRatio="none">
      <path d="M230 0 H212 C222 40 214 86 186 120 H230 Z" fill="var(--brand-red)"/>
      <path d="M230 76 C220 98 206 112 196 120 H230 Z" fill="var(--brand-green)"/>
    </svg>
    <div class="brand"><span class="brand-mark"></span>RKT Builders</div>
    <div class="envelope-return">
      P.O. BOX 817<br>
      Harlow Point, MD 20999
    </div>
  </section>

</body>
</html>
```